Calvin Pruett Insurance Biz Card
Biz card and stationary
Calvin Pruett Insurance Biz Card - Financial Services
Creative Brief
Professional
Calvin Pruett
Independent Agent
Greensboro, NC
pruettgroup@lanvex.example.net
www.calvinpruettinsurance.example.com
please use the logo we upload, and keep all font at a size 9 or 10.
please use the content we upload for an example of the back of the card

```html
<!DOCTYPE html>
<html lang="en">
<head>
<meta charset="utf-8">
<title>Calvin Pruett Insurance – Business Card</title>
<link rel="stylesheet" href="https://fonts.googleapis.com/css2?family=Crimson+Pro:wght@400;600;700&display=swap">
<style>
  :root {
    --navy: #1c2b5f;
    --grey-text: #9b9b9b;
    --grey-curve: #b9b9b9;
    --ink: #2a2a2a;
    --card: #ffffff;
    --backdrop: #ecebe8;
    --divider: #d8d8d8;
  }
  * { margin: 0; padding: 0; box-sizing: border-box; }
  html, body {
    width: 1200px; height: 778px; overflow: hidden;
    background: var(--backdrop);
  }
  .card {
    position: absolute; left: 75px; top: 89px;
    width: 1050px; height: 600px;
    background: var(--card);
    overflow: hidden;
    box-shadow: 0 6px 18px rgba(0,0,0,0.12);
    font-family: "Crimson Pro", Georgia, serif;
  }
  .card-swooshes { position: absolute; inset: 0; }
  .brand {
    position: absolute; left: 263px; top: 58px;
    display: flex; align-items: center; gap: 22px;
  }
  .brand-square { width: 117px; height: 117px; background: var(--navy); flex: none; }
  .brand-name {
    color: var(--navy); font-weight: 700; font-size: 48px; line-height: 0.98;
  }
  .agent {
    position: absolute; right: 550px; top: 272px; text-align: right;
    white-space: nowrap;
  }
  .agent-name { color: var(--navy); font-weight: 700; font-size: 38px; line-height: 1.1; }
  .agent-title { color: var(--grey-text); font-size: 28px; line-height: 1.15; letter-spacing: 0.3px; }
  .divider {
    position: absolute; left: 530px; top: 250px; width: 1px; height: 170px;
    background: var(--divider);
  }
  .contact {
    position: absolute; left: 556px; top: 262px; color: var(--ink);
    white-space: nowrap;
  }
  .contact-city { font-size: 28px; line-height: 1.2; margin-bottom: 22px; }
  .contact-line {
    display: flex; align-items: center; gap: 9px;
    font-size: 24px; line-height: 1.3;
  }
  .contact-icon { width: 15px; height: 15px; flex: none; fill: var(--navy); }
</style>
</head>
<body>
  <div class="card">
    <svg class="card-swooshes" viewBox="0 0 1050 600" aria-hidden="true">
      <path fill="var(--grey-curve)" d="M800 0 C960 100 1030 300 1050 565 L1050 530 C1040 330 980 110 840 0 Z"/>
      <path fill="var(--navy)" d="M840 0 L1050 0 L1050 530 C1040 330 980 110 840 0 Z"/>
      <path fill="var(--grey-curve)" d="M0 295 C50 470 170 580 325 600 L270 600 C140 570 40 470 0 330 Z"/>
      <path fill="var(--navy)" d="M0 330 C40 470 140 570 270 600 L0 600 Z"/>
    </svg>

    <div class="brand">
      <div class="brand-square"></div>
      <div class="brand-name">Calvin Pruett<br>Insurance, LLC</div>
    </div>

    <div class="agent">
      <div class="agent-name">Calvin Pruett</div>
      <div class="agent-title">Independent Agent</div>
    </div>

    <div class="divider"></div>

    <div class="contact">
      <div class="contact-city">Greensboro, NC</div>
      <div class="contact-line">
        <svg class="contact-icon" viewBox="0 0 20 20"><path d="M5 1c1 0 2 3 2 4s-2 1.5-2 2.5c0 2 4 7 6.5 7.5 1 0 1.5-2 2.5-2s4 1 4 2-2 4-4 4C7 19 1 11 1 5c0-2 2-4 4-4z"/></svg>
        <span>336-555-0148</span>
      </div>
      <div class="contact-line">
        <svg class="contact-icon" viewBox="0 0 20 20"><path d="M1 4h18v12H1z M2.5 5.5 10 11l7.5-5.5" fill="none" stroke="var(--navy)" stroke-width="2"/></svg>
        <span>pruettgroup@lanvex.example.net</span>
      </div>
      <div class="contact-line">
        <svg class="contact-icon" viewBox="0 0 20 20"><circle cx="10" cy="10" r="9"/><path d="M1 10h18M10 1c-4 5-4 13 0 18M10 1c4 5 4 13 0 18" fill="none" stroke="#fff" stroke-width="1.3"/></svg>
        <span>www.calvinpruettinsurance.example.com</span>
      </div>
    </div>
  </div>
</body>
</html>
```